Meadowbrook Setter Society - Rare dog breed club needs web design!

The Transylvanian Hound (or Erdélyi kopó) is an ancient Hungarian dog breed. These medium-sized hounds were favored by the Hungarian kings and princes for hunting bears and wolves in the Carpathian mountains of Transylvania. The breed's great adaptability to the region's extreme climates of sweltering summers and frigid winters made it an excellent all season hunting dog. This dog has a sleek appearance and stunning good looks. They are lean, appear very elegant and proud. Their erect posture and beautifully sculpted head portray great attentiveness and authority. In general, this rare breed is extremely good natured, loyal and obedient. It has a tendency to form strong attachments to its primary caretakers and will remain loyal and protective. (Please refer to existing web resources.)

The Meadowbrook Setter Society - with current website www.meadowbrooksetter-example.org - is the official breed club of Transylvanian Hound afficionados, breeders and owners in the United States, which was founded in 2010. We are looking for a web design for the new, upgraded version of this central (currenty non-functioning) website. Please do not recycle the old logo (we may choose from your suggesions and pay for it!) or any of the old texts. Please use the structure described below. Overall, the webpage serves a dual purpose: an educational one (about the breed itself) and a community-building one (inside the Club). The proposed structure of the website is as follows:

1. About the Kopó
- Breed History
- Breed Standard
- Public Education
- Photo Gallery

2. Life with a Kopó
- Health and Genetics
- Feeding and Nutrition
- Training and Activities

3. Finding a Kopó
- Is this the Right Breed for You?
- Choosing a Puppy
- FAQ
- Breeder Referral

4. The Meadowbrook Setter Society
- Constituton
- Officers and Appointees
- Code of Ethics
- Breeder Guidelines
- Membership
- Reports
- Links

5. News and Events

6. Shop

We are attaching a couple of examples of the graphics/drawings of the dogs that would be part of the design of the website. We plan to have more of these artistic depictions, nicely embedded into the background (maybe shaded out at the edges just like the drawings themselves) and less actual photos. Or a good combination of the two.

Further information upon request.

Reason: There are a few very promising design collaborations ongoing. As we moved the brief to a more artistic and graphic direction, we felt that one week of extension would be needed to get to the perfect end-product, which could include designs for sub-pages as well.

Reason: In order to make the final modifications to the leading designs, and at the request of those designers, the deadline is extended until Friday.

Target Market(s)

- MBSS Club members, dog (especially T-Hound) owners, past and future owners, breeders, puppy buyers, hunters, kennel clubs, dog show participants, vets, animal shelters, Hungarian, Romanian and other European web visitors, historians

Industry/Entity Type

Club

Font styles to use
Serif
Decorative
Script

Requirements
Must have
• - Sync with graphics of dogs (see attachments), but accentuate the rich black basic color of the dogs
- Elegance, aristocratic/noble look and feel (but not overly archaic)
- Love, companionship, dogs as family members
- Hunting usage, but no bloody associations, rather romantic ones
- Simple to use and navigate for non-web-natives
- Old world (Central European) atmosphere, even the exotic, rustic and romantic Transylvanian feel - SEE the new attachment for inspiration (this was a design plan which we discarded (mainly because of its gothic, (nazi-like), unreadable font, and the fact that the plan makes the black-looking dogs appear brown), however we loved the fact that it was not full of boxes/windows, had a marble/sand stone like continuous background, lots of little elegant graphics, the drawings embedded, etc.
Nice to have
• - Working on smartphone, iPads, etc., so dynamic website design
- Web shop to be added to functionalities in the future (?)
- English language for now, in the future can be Hungarian, Romanian, etc., so the font choice should handle various alphabets
- Focus on the dogs (likely more graphics than photos, at least on the main pages), and not on the activities/humans - the design should accentuate the black and not the tan of the graphics!
Should not have
• - Old logo from the old www.meadowbrooksetter-example.org webpage or the other logo from the Chatterbox site of the Meadowbrook Setter Society, we will have a new one (maybe designed by you!)
- Breed club, kennel club cliches
- Cutesy, adorable, cheesy design elements
- Old, stale, monolithic, archaic, snobbish, etc. look and feel
- No vampire associations

```html
<!DOCTYPE html>
<html lang="en">
<head>
<meta charset="utf-8">
<title>Meadowbrook Setter Society</title>
<link rel="stylesheet" href="https://fonts.googleapis.com/css2?family=Cinzel:wght@400;700&family=Pinyon+Script&family=Open+Sans:wght@400&display=swap">
<style>
  :root {
    --page-black: #0a0a0a;
    --band-black: #050505;
    --gold: #e2b94e;
    --gold-pale: #ead291;
    --gold-deep: #b8862e;
    --gold-text: #c89a3c;
    --parchment: #e8dcc6;
    --parchment-edge: #d6c6a8;
    --ink: #3a2e25;
    --footer-white: #f1ead8;
  }
  * { margin: 0; padding: 0; box-sizing: border-box; }
  html, body { width: 1200px; height: 981px; overflow: hidden; }
  body {
    position: relative;
    background: radial-gradient(ellipse at 50% 40%, #161616 0%, var(--page-black) 70%);
    font-family: "Cinzel", serif;
    color: var(--gold);
  }

  .nav-band {
    position: absolute; left: 95px; top: 66px; width: 1015px; height: 52px;
    background: var(--band-black);
    border-top: 1px solid rgba(226,185,78,.45);
    border-bottom: 1px solid rgba(226,185,78,.45);
  }
  .nav-link {
    position: absolute; top: 12px;
    font-size: 13px; line-height: 14px; letter-spacing: .5px;
    color: var(--gold); text-decoration: none; text-transform: uppercase;
  }

  .brand {
    position: absolute; left: 470px; top: 22px; width: 260px; height: 150px;
    background: var(--band-black);
    border: 2px solid var(--gold-deep);
    border-radius: 0 0 130px 130px;
    text-align: center;
    z-index: 3;
  }
  .brand-dot {
    display: block; width: 34px; height: 34px; margin: 16px auto 10px;
    border-radius: 50%; background: var(--gold);
  }
  .brand-name {
    font-size: 17px; line-height: 21px; color: var(--gold); font-weight: 400;
    text-transform: uppercase; letter-spacing: 1px;
  }

  .hero-photo {
    position: absolute; left: 462px; top: 172px; width: 585px; height: 293px;
    background: radial-gradient(ellipse at 60% 60%, #2a1d12 0%, #160f0a 45%, rgba(10,10,10,0) 75%);
    z-index: 1;
  }

  .welcome { position: relative; z-index: 2; }
  .welcome-script {
    position: absolute; left: 133px; top: 198px;
    font-family: "Pinyon Script", cursive; font-size: 62px; line-height: 80px;
    color: var(--gold-pale);
  }
  .welcome-title {
    position: absolute; left: 137px; top: 268px; white-space: nowrap;
    font-size: 26px; line-height: 32px; letter-spacing: .5px;
    color: var(--gold-pale); text-transform: uppercase; font-weight: 400;
  }
  .welcome-intro {
    position: absolute; left: 141px; top: 315px; width: 400px;
    font-family: "Open Sans", sans-serif; font-size: 14px; line-height: 17px;
    color: var(--gold-text);
  }

  .intro-panel { position: absolute; left: 110px; top: 465px; width: 980px; height: 360px; z-index: 2; }
  .intro-panel svg { position: absolute; inset: 0; }
  .panel-drawing {
    position: absolute; left: 14px; top: 30px; width: 262px; height: 320px;
    background: radial-gradient(ellipse at 50% 50%, #8c7864 0%, #b8a58a 45%, rgba(232,220,198,0) 72%);
  }
  .panel-copy {
    position: absolute; left: 282px; top: 76px; width: 680px;
    font-size: 13.6px; line-height: 17px; color: var(--ink);
  }
  .panel-copy p { margin-bottom: 17px; }
  .panel-copy .initial { font-size: 24px; line-height: 17px; }

  .footer-line {
    position: absolute; left: 95px; width: 1040px; height: 1px;
    background: linear-gradient(90deg, rgba(226,185,78,0), rgba(226,185,78,.6) 50%, rgba(226,185,78,0));
  }
  .footer-ornament {
    position: absolute; left: 535px; top: 862px; width: 132px; height: 38px;
    background: radial-gradient(ellipse at 50% 50%, #c9973f 0%, #7a5520 45%, rgba(10,10,10,0) 75%);
  }
  .footer-copy {
    position: absolute; top: 897px; font-size: 12.5px; line-height: 16px; color: var(--gold);
  }
  .footer-copy.left { left: 129px; }
  .footer-copy.right { right: 120px; }
  .footer-copy .email { color: var(--footer-white); }
</style>
</head>
<body>
  <header>
    <nav class="nav-band">
      <a class="nav-link" style="left:67px" href="#">About<br>the Kopó</a>
      <a class="nav-link" style="left:167px" href="#">Life with<br>a Kopó</a>
      <a class="nav-link" style="left:264px" href="#">Finding<br>a Kopó</a>
      <a class="nav-link" style="left:688px" href="#">The MBSS</a>
      <a class="nav-link" style="left:791px" href="#">News and<br>Events</a>
      <a class="nav-link" style="left:920px" href="#">Shop</a>
    </nav>
    <div class="brand">
      <span class="brand-dot"></span>
      <div class="brand-name">Meadowbrook<br>Setter<br>Society</div>
    </div>
  </header>

  <main>
    <div class="hero-photo" role="img" aria-label="Photo of three black and tan Transylvanian Hounds sitting together"></div>

    <section class="welcome">
      <div class="welcome-script">Welcome to</div>
      <h1 class="welcome-title">Meadowbrook Setter Society</h1>
      <p class="welcome-intro">The official breed club of Transylvanian Hound afficionados, breeders and owners in the United States, which was founded in 2010</p>
    </section>

    <section class="intro-panel">
      <svg width="980" height="360" viewBox="0 0 980 360" aria-hidden="true">
        <defs>
          <linearGradient id="parchment-fill" x1="0" y1="0" x2="1" y2="1">
            <stop offset="0" stop-color="#efe5d2"/>
            <stop offset="1" stop-color="#e0d2b8"/>
          </linearGradient>
          <linearGradient id="frame-gold" x1="0" y1="0" x2="1" y2="1">
            <stop offset="0" stop-color="#f0d48a"/>
            <stop offset=".5" stop-color="#b8862e"/>
            <stop offset="1" stop-color="#e6c574"/>
          </linearGradient>
        </defs>
        <path d="M30 0 H950 A30 30 0 0 0 980 30 V330 A30 30 0 0 0 950 360 H30 A30 30 0 0 0 0 330 V30 A30 30 0 0 0 30 0 Z" fill="url(#frame-gold)"/>
        <path d="M36 8 H944 A28 28 0 0 0 972 36 V324 A28 28 0 0 0 944 352 H36 A28 28 0 0 0 8 324 V36 A28 28 0 0 0 36 8 Z" fill="#1a140c"/>
        <path d="M40 12 H940 A28 28 0 0 0 968 40 V320 A28 28 0 0 0 940 348 H40 A28 28 0 0 0 12 320 V40 A28 28 0 0 0 40 12 Z" fill="url(#parchment-fill)" stroke="#b8862e" stroke-width="2"/>
      </svg>
      <div class="panel-drawing" role="img" aria-label="Pencil drawing of two Transylvanian Hounds in profile"></div>
      <div class="panel-copy">
        <p><span class="initial">T</span>he Transylvanian Hound (or Erdélyi kopó) is an ancient Hungarian dog breed. These medium-sized hounds were favored by the Hungarian kings and princes for hunting bears and wolves in the Carpathian mountains of Transylvania.</p>
        <p>The breed’s great adaptability to the region’s extreme climates of sweltering summers and frigid winters made it an excellent all season hunting dog. This dog has a sleek appearance and stunning good looks. They are lean, appear very elegant and proud. Their erect posture and beautifully sculpted head portray great attentiveness and authority. In general, this rare breed is extremely good natured, loyal and obedient.</p>
        <p>It has a tendency to form strong attachments to its primary caretakers and will remain loyal and protective.</p>
      </div>
    </section>
  </main>

  <footer>
    <div class="footer-line" style="top:879px"></div>
    <div class="footer-ornament" role="img" aria-label="Gold scroll ornament"></div>
    <p class="footer-copy left">© 2014. meadowbrook setter society. All Rights Reserved.</p>
    <p class="footer-copy right">contact: <span class="email">info@meadowbrooksetter-example.org</span></p>
    <div class="footer-line" style="top:930px"></div>
  </footer>
</body>
</html>
```